Business Card for By Marcus Hale

Looking to have a business card designed for my lifestyle and fitness company. My company offers personal training, online programming and nutrition advice based out of London, United Kingdom.

I'd like to see modern, sleek designs, focusing on black, matte black or matte grey. Design doesn't need to be overly descriptive as this will also be used as a personal business card. I've included my logo.

Please note that my company is no longer called "By Marcus Hale" but instead "By Marcus Hale", this is because of my other ventures. Therefore please don't use the "fitness by marcus hale" text.

information about my company can be found at www.bymarcushale.com

Company is also based out of London (United Kingdom) & Sydney (Australia) this could be reflected on the card.

Industry/Entity Type

Business

Contact Information for Business Card

Marcus Hale
+44 7382 615204
marcus@bymarcushale.com
www.bymarcushale.com

Font styles to use
Sans Serif

Requirements
Must have
• All contact details and inclusion of my logo.

```html
<!DOCTYPE html>
<html lang="en">
<head>
<meta charset="utf-8">
<title>By Marcus Hale — Business Card</title>
<link href="https://fonts.googleapis.com/css2?family=Roboto:wght@400;700&display=swap" rel="stylesheet">
<style>
  :root {
    --stage: #2a2a2c;
    --card-black: #1c1b1c;
    --card-black-soft: #262425;
    --paper: #ffffff;
    --ink: #1a1a1a;
    --muted: #d9d9d9;
  }
  * { box-sizing: border-box; margin: 0; padding: 0; }
  html, body { width: 1200px; height: 800px; overflow: hidden; }
  body {
    background: var(--stage);
    font-family: "Roboto", Arial, sans-serif;
    position: relative;
  }
  .card {
    position: absolute;
    width: 520px;
    height: 297px;
    border-radius: 3px;
    overflow: hidden;
    box-shadow: 0 14px 30px rgba(0,0,0,0.45);
  }

  /* Front */
  .card-front {
    left: 90px; top: 90px;
    background: radial-gradient(ellipse at 45% 40%, var(--card-black-soft), var(--card-black) 70%);
    color: var(--paper);
  }
  .brand {
    position: absolute;
    display: flex;
    align-items: center;
    gap: 10px;
    white-space: nowrap;
  }
  .brand-mark {
    width: 14px; height: 14px;
    background: currentColor;
    flex: none;
  }
  .brand-name {
    font-weight: 700;
    text-transform: uppercase;
    letter-spacing: 1px;
    font-size: 20px;
  }
  .card-front .brand {
    left: 0; right: 0;
    justify-content: center;
    top: 110px;
  }
  .rule-row {
    position: absolute;
    left: 0; right: 0;
    display: flex;
    align-items: center;
    justify-content: center;
    gap: 12px;
  }
  .bar {
    width: 44px; height: 1px;
    background: var(--paper);
    position: relative;
  }
  .bar::before, .bar::after {
    content: "";
    position: absolute;
    top: -3px;
    width: 2px; height: 7px;
    background: var(--paper);
  }
  .bar::before { left: 0; }
  .bar::after { right: 0; }
  .card-front .rule-top { top: 150px; }
  .card-front .rule-top .bar { width: 150px; }
  .front-web {
    font-size: 11px;
    letter-spacing: 1.6px;
    color: var(--muted);
  }
  .card-front .rule-web { top: 212px; }

  /* Back */
  .card-back {
    left: 590px; top: 413px;
    background: var(--card-black);
  }
  .card-back svg.sweep { position: absolute; inset: 0; }
  .card-back .brand {
    left: 44px;
    top: 136px;
    color: var(--ink);
  }
  .card-back .brand-name { font-size: 18px; }
  .contact {
    position: absolute;
    right: 22px;
    top: 82px;
    text-align: right;
    color: var(--paper);
  }
  .contact-name {
    font-weight: 700;
    font-size: 13px;
    letter-spacing: 0.5px;
    text-transform: uppercase;
    margin-bottom: 14px;
    margin-right: 24px;
  }
  .contact-line {
    display: flex;
    justify-content: flex-end;
    align-items: center;
    gap: 8px;
    font-size: 11px;
    line-height: 1;
    margin-bottom: 8px;
  }
  .contact-icon {
    width: 16px; height: 16px;
    flex: none;
  }
</style>
</head>
<body>

  <section class="card card-front" aria-label="Card front">
    <div class="brand">
      <span class="brand-mark"></span>
      <span class="brand-name">By Marcus Hale</span>
    </div>
    <div class="rule-row rule-top"><span class="bar"></span></div>
    <div class="rule-row rule-web">
      <span class="bar"></span>
      <span class="front-web">www.BYMARCUSHALE.com</span>
      <span class="bar"></span>
    </div>
  </section>

  <section class="card card-back" aria-label="Card back">
    <svg class="sweep" viewBox="0 0 520 297" width="520" height="297" aria-hidden="true">
      <path d="M0,0 H330 Q305,215 30,297 H0 Z" fill="var(--paper)"/>
      <path d="M356,0 Q330,230 62,297" fill="none" stroke="var(--paper)" stroke-width="2"/>
    </svg>
    <div class="brand">
      <span class="brand-mark"></span>
      <span class="brand-name">By Marcus Hale</span>
    </div>
    <div class="contact">
      <p class="contact-name">Marcus Hale</p>
      <p class="contact-line">+44 7382 615204
        <svg class="contact-icon" viewBox="0 0 16 16" aria-hidden="true">
          <circle cx="8" cy="8" r="7" fill="none" stroke="#fff" stroke-width="1"/>
          <rect x="5.5" y="3.5" width="5" height="9" rx="1" fill="none" stroke="#fff" stroke-width="1"/>
        </svg>
      </p>
      <p class="contact-line">marcus@bymarcushale.com
        <svg class="contact-icon" viewBox="0 0 16 16" aria-hidden="true">
          <circle cx="8" cy="8" r="7" fill="none" stroke="#fff" stroke-width="1"/>
          <rect x="4" y="5" width="8" height="6" fill="none" stroke="#fff" stroke-width="1"/>
          <path d="M4,5 L8,8.5 L12,5" fill="none" stroke="#fff" stroke-width="1"/>
        </svg>
      </p>
      <p class="contact-line">www.bymarcushale.com
        <svg class="contact-icon" viewBox="0 0 16 16" aria-hidden="true">
          <circle cx="8" cy="8" r="7" fill="none" stroke="#fff" stroke-width="1"/>
          <circle cx="8" cy="8" r="4" fill="none" stroke="#fff" stroke-width="1"/>
          <ellipse cx="8" cy="8" rx="1.8" ry="4" fill="none" stroke="#fff" stroke-width="0.8"/>
          <path d="M4,8 H12" stroke="#fff" stroke-width="0.8"/>
        </svg>
      </p>
    </div>
  </section>

</body>
</html>
```